Design some Business Cards

I need a business card that goes with my current website looks, i have a mockup which i am sending, the idea i have is to be very clean in the front, and in the back all my skills as developer, kind of tavorly skills.

My website si davremonte.com

```html
<!DOCTYPE html>
<html lang="en">
<head>
<meta charset="utf-8">
<title>Mateo Ruvalcaba – Business Cards</title>
<link href="https://fonts.googleapis.com/css2?family=Lato:wght@400;700&display=swap" rel="stylesheet">
<style>
  :root {
    --bg: #5a5a5a;
    --orange: #f07418;
    --orange-dark: #d85a14;
    --white: #ffffff;
    --paper: #f7f7f7;
    --ink: #1c1c1c;
    --green: #1e9c3a;
    --photo-a: #e9d6b5;
    --photo-b: #8a6a52;
  }
  * { box-sizing: border-box; margin: 0; padding: 0; }
  html, body {
    width: 1200px; height: 900px; overflow: hidden;
    background: var(--bg);
    font-family: "Lato", sans-serif;
  }
  .stage {
    position: relative; width: 1200px; height: 900px;
    display: flex; flex-direction: column; align-items: center; justify-content: center; gap: 44px;
  }
  .card {
    position: relative; width: 660px; height: 377px;
    border-radius: 28px; overflow: hidden;
    background: var(--white);
    box-shadow: 0 10px 24px rgba(0,0,0,.35);
  }
  .photo {
    position: absolute; width: 170px; height: 170px; border-radius: 50%;
    border: 6px solid var(--ink);
    background: radial-gradient(circle at 50% 40%, var(--photo-a) 0%, #c9a37f 45%, var(--photo-b) 100%);
  }
  .name { font-weight: 700; font-size: 30px; color: var(--ink); letter-spacing: .2px; white-space: nowrap; }
  .role { font-size: 21px; color: var(--ink); margin-top: 2px; white-space: nowrap; }

  /* Front card */
  .front { background: var(--paper); }
  .front .edge { position: absolute; left: 0; top: 0; width: 60px; height: 100%; }
  .front .photo { left: 88px; top: 46px; }
  .front .identity { position: absolute; left: 282px; top: 92px; }
  .front .role { display: inline-block; padding-bottom: 6px; border-bottom: 3px solid var(--green); }
  .front .web-tab {
    position: absolute; left: 0; bottom: 0; width: 330px; height: 64px;
    background: var(--orange); border-top-right-radius: 32px;
    display: flex; align-items: center; padding-left: 96px;
    font-weight: 700; font-size: 19px; color: var(--ink);
  }
  .front .web-tab::before {
    content: ""; position: absolute; left: 0; top: 0; width: 60px; height: 100%;
    background: var(--orange-dark);
  }

  /* Back card */
  .back .panel { position: absolute; left: 0; top: 0; width: 300px; height: 100%; }
  .back .skills { position: absolute; left: 70px; top: 38px; color: var(--white); }
  .back .skills h2 {
    font-weight: 400; font-size: 30px; display: inline-block;
    padding-bottom: 4px; border-bottom: 3px solid var(--ink);
  }
  .back .skills ul { list-style: none; margin-top: 12px; }
  .back .skills li {
    font-size: 18px; line-height: 30px; position: relative; padding-left: 26px; white-space: nowrap;
  }
  .back .skills li::before {
    content: ""; position: absolute; left: 0; top: 10px;
    border-left: 12px solid var(--ink); border-top: 6px solid transparent; border-bottom: 6px solid transparent;
  }
  .back .identity { position: absolute; right: 44px; top: 56px; text-align: right; }
  .back .photo { left: 390px; top: 150px; }
</style>
</head>
<body>
<main class="stage">

  <section class="card front" aria-label="Business card front">
    <svg class="edge" viewBox="0 0 60 377" preserveAspectRatio="none" aria-hidden="true">
      <rect x="0" y="0" width="36" height="377" fill="var(--orange-dark)"/>
      <rect x="36" y="0" width="24" height="377" fill="var(--orange)"/>
    </svg>
    <div class="photo" role="img" aria-label="Portrait photo of Mateo Ruvalcaba"></div>
    <div class="identity">
      <div class="name">Mateo Ruvalcaba</div>
      <div class="role">Full Stack Developer</div>
    </div>
    <div class="web-tab">www.davremonte.com</div>
  </section>

  <section class="card back" aria-label="Business card back">
    <svg class="panel" viewBox="0 0 300 377" preserveAspectRatio="none" aria-hidden="true">
      <polygon points="0,0 300,0 240,377 0,377" fill="var(--orange)"/>
      <rect x="0" y="0" width="36" height="377" fill="var(--orange-dark)"/>
    </svg>
    <div class="skills">
      <h2>skills like:</h2>
      <ul>
        <li>Web Frameworks</li>
        <li>Server Apps</li>
        <li>Markup, Styles</li>
        <li>Build Tooling</li>
        <li>Scripting + VCS</li>
        <li>Test Driven Dev</li>
      </ul>
    </div>
    <div class="identity">
      <div class="name">Mateo Ruvalcaba</div>
      <div class="role">Full Stack Developer</div>
    </div>
    <div class="photo" role="img" aria-label="Portrait photo of Mateo Ruvalcaba"></div>
  </section>

</main>
</body>
</html>
```